Flyerdesign for a Sports Homepage

I need a design for our Merchandise/Discount Flyer.
we are going to sell high class sports equipment.
the flyer should be in Size A5 or between A5 and A4.
there should be mentioned our Product names:
Product name for powerlifting: Torvik
Product name for Boxing: ZL Boxing
Product name for Martial Arts: Murelt
Product name for MMA: PitVolt
Product name for Bodybuilding: Bramfold

our Storename: PushAndDuel
Homepage: www.pushandduel.example

there should be space for entering a discount code
shop logo and brand logos: all pictures are attached.

out of the box thinking is welcome

Target Market(s)

People who do powersports like powerlifting or mma

Industry/Entity Type

Sport

Requirements
Must have
• 2 sides, all our brandnames, homepage, shop name and sports

```html
<!DOCTYPE html>
<html lang="en">
<head>
<meta charset="utf-8">
<title>PushAndDuel – Discount Flyer</title>
<link rel="stylesheet" href="https://fonts.googleapis.com/css2?family=Oswald:wght@400;500;600&family=Roboto+Condensed:wght@400;700&display=swap">
<style>
  :root {
    --page: #dcdcdc;
    --ink: #0b0b0b;
    --panel: #141414;
    --panel-soft: #232323;
    --gold: #c9a94a;
    --gold-light: #e9d27c;
    --gold-deep: #8c6d22;
    --white: #ffffff;
    --grey: #9a9a9a;
  }
  * { box-sizing: border-box; margin: 0; padding: 0; }
  html, body { width: 845px; height: 1200px; overflow: hidden; }
  body { background: var(--page); position: relative; font-family: "Oswald", "Roboto Condensed", sans-serif; }

  .flyer {
    position: absolute; left: 70px; width: 726px; height: 512px; overflow: hidden;
    background: radial-gradient(ellipse at 60% 45%, var(--panel-soft), var(--ink) 75%);
  }
  .flyer--front { top: 70px; }
  .flyer--back { top: 625px; }

  .flyer__decor { position: absolute; inset: 0; width: 726px; height: 512px; }

  .photo { position: absolute; }
  .photo--athlete-woman {
    left: 0; top: 108px; width: 380px; height: 350px;
    background: radial-gradient(ellipse at 45% 45%, #8a7a6a 0%, #4a4038 35%, #1a1714 75%);
  }
  .photo--athlete-man {
    left: 470px; top: 34px; width: 256px; height: 418px;
    background: radial-gradient(ellipse at 40% 40%, #7a6555 0%, #3c3029 40%, #141110 80%);
  }

  .brand { position: absolute; left: 18px; top: 16px; width: 105px; height: 85px;
    border: 1px solid var(--gold-deep); background: #111;
    display: flex; align-items: center; justify-content: center; gap: 6px; }
  .brand__square { width: 10px; height: 10px; background: var(--gold); }
  .brand__name { color: var(--gold); font-weight: 500; font-size: 13px; letter-spacing: .3px; }

  .tagline { position: absolute; left: 138px; top: 20px; color: var(--gold); font-weight: 500;
    font-size: 16.5px; line-height: 25px; text-transform: uppercase; }

  .social { position: absolute; right: 22px; top: 12px; display: flex; gap: 11px; }
  .social__dot { width: 15px; height: 15px; border: 1.5px solid var(--white); border-radius: 50%; }

  .medallion { position: absolute; border-radius: 50%;
    background: linear-gradient(145deg, var(--gold-light), var(--gold-deep) 55%, var(--gold-light));
    padding: 5px; }
  .medallion__art { width: 100%; height: 100%; border-radius: 50%; border: 2px solid #2a2a2a;
    background: radial-gradient(circle at 50% 55%, #ff8a1c 0%, #c8330e 35%, #3a0d08 75%); }

  .front-title { position: absolute; right: 23px; top: 104px; color: var(--gold);
    font-weight: 500; font-size: 33px; letter-spacing: .5px; }
  .product-list { position: absolute; right: 23px; top: 166px; list-style: none; text-align: right; }
  .product-list li { color: var(--white); font-family: "Roboto Condensed", sans-serif; font-weight: 700;
    font-size: 14.5px; height: 36.7px; }
  .product-list b { font-family: "Oswald", sans-serif; color: var(--gold); font-weight: 500; font-size: 17px; }

  .discount { position: absolute; right: 23px; top: 356px; font-weight: 500; font-size: 44px; line-height: 56px; color: var(--white); }
  .discount__amount { color: var(--gold); }
  .discount-code { position: absolute; right: 23px; top: 416px; color: var(--grey);
    font-family: "Roboto Condensed", sans-serif; font-weight: 700; font-size: 14px; letter-spacing: 1.4px; }

  .collections-title { position: absolute; left: 22px; top: 134px; color: var(--gold); font-weight: 500; font-size: 29px; }
  .collections-text { position: absolute; left: 22px; top: 182px; width: 400px; color: var(--white);
    font-family: "Roboto Condensed", sans-serif; font-size: 13.5px; line-height: 17px; }
  .collections-text p + p { margin-top: 9px; }

  .range { position: absolute; top: 289px; text-align: center; width: 116px; }
  .range .medallion { position: static; width: 116px; height: 116px; margin: 0 auto; }
  .range__name { margin-top: 10px; color: var(--gold); font-weight: 500; font-size: 15px; line-height: 16px; }
  .range__sport { color: var(--white); font-family: "Roboto Condensed", sans-serif; font-size: 11.5px; text-transform: uppercase; }

  .footer { position: absolute; left: 0; bottom: 0; width: 726px; height: 48px; }
  .footer__contact { position: absolute; left: 20px; top: 15px; display: flex; align-items: center; gap: 7px;
    color: var(--white); font-family: "Roboto Condensed", sans-serif; font-weight: 700; font-size: 12.5px; }
  .footer__contact svg { flex: none; }
  .footer__gap { width: 14px; }
  .footer__web { position: absolute; right: 24px; top: 14px; display: flex; align-items: center; gap: 9px;
    color: var(--ink); font-weight: 500; font-size: 15px; letter-spacing: 1px; text-transform: uppercase; }
</style>
</head>
<body>

<section class="flyer flyer--front">
  <div class="photo photo--athlete-woman" role="img" aria-label="Photo of a female athlete lifting dumbbells, seen from behind"></div>
  <svg class="flyer__decor" viewBox="0 0 726 512" aria-hidden="true">
    <defs>
      <linearGradient id="goldBand" x1="0" y1="0" x2="1" y2="1">
        <stop offset="0" stop-color="#e9d27c"/><stop offset="1" stop-color="#8c6d22"/>
      </linearGradient>
    </defs>
    <rect x="0" y="0" width="726" height="107" fill="#0b0b0b"/>
    <polygon points="460,40 500,40 265,458 225,458" fill="url(#goldBand)" opacity=".75"/>
    <polyline points="0,107 400,107 440,40 726,40" fill="none" stroke="#c9a94a" stroke-width="2.5"/>
    <polygon points="0,464 726,464 726,512 0,512" fill="#0b0b0b"/>
    <line x1="0" y1="458" x2="726" y2="458" stroke="#c9a94a" stroke-width="2.5"/>
    <polygon points="490,464 726,464 726,512 468,512" fill="url(#goldBand)"/>
  </svg>

  <div class="brand"><span class="brand__square"></span><span class="brand__name">PushAndDuel</span></div>
  <p class="tagline">Premium quality<br>products for all lifting<br>and fighting sports</p>
  <div class="social"><span class="social__dot"></span><span class="social__dot"></span><span class="social__dot"></span></div>

  <div class="medallion" style="left:366px;top:107px;width:96px;height:96px"><div class="medallion__art" role="img" aria-label="PitVolt brand artwork"></div></div>
  <div class="medallion" style="left:310px;top:211px;width:96px;height:96px"><div class="medallion__art" role="img" aria-label="Torvik brand artwork"></div></div>
  <div class="medallion" style="left:247px;top:317px;width:96px;height:96px"><div class="medallion__art" role="img" aria-label="Bramfold brand artwork"></div></div>

  <h1 class="front-title">PUSH AND DUEL</h1>
  <ul class="product-list">
    <li>Product name for powerlifting: <b>TORVIK</b></li>
    <li>Product name for Boxing: <b>ZL BOXING</b></li>
    <li>Product name for Martial Arts: <b>MURELT</b></li>
    <li>Product name for MMA: <b>PITVOLT</b></li>
    <li>Product name for Bodybuilding: <b>BRAMFOLD</b></li>
  </ul>
  <p class="discount"><span class="discount__amount">€50,00</span> DISCOUNT</p>
  <p class="discount-code">ENTERING A DISCOUNT CODE: 0000 000</p>

  <footer class="footer">
    <div class="footer__contact">
      <svg width="9" height="12" viewBox="0 0 9 12"><path d="M4.5 0A4.5 4.5 0 0 0 0 4.5C0 8 4.5 12 4.5 12S9 8 9 4.5A4.5 4.5 0 0 0 4.5 0zm0 6.3a1.8 1.8 0 1 1 0-3.6 1.8 1.8 0 0 1 0 3.6z" fill="#c9a94a"/></svg>
      <span>NORVAK UG Lindenweg 4, 01234 Musterstadt</span>
      <span class="footer__gap"></span>
      <svg width="13" height="9" viewBox="0 0 13 9"><rect width="13" height="9" fill="#c9a94a"/><path d="M0 0l6.5 5L13 0" stroke="#0b0b0b" fill="none"/></svg>
      <span>info@norvak.example</span>
    </div>
    <div class="footer__web">
      <svg width="16" height="16" viewBox="0 0 16 16"><circle cx="8" cy="8" r="7" fill="none" stroke="#0b0b0b" stroke-width="1.6"/><ellipse cx="8" cy="8" rx="3" ry="7" fill="none" stroke="#0b0b0b" stroke-width="1.2"/><line x1="1" y1="8" x2="15" y2="8" stroke="#0b0b0b" stroke-width="1.2"/></svg>
      <span>www.pushandduel.example</span>
    </div>
  </footer>
</section>

<section class="flyer flyer--back">
  <div class="photo photo--athlete-man" role="img" aria-label="Photo of a muscular male athlete lifting a barbell"></div>
  <svg class="flyer__decor" viewBox="0 0 726 512" aria-hidden="true">
    <defs>
      <linearGradient id="goldBandBack" x1="0" y1="0" x2="1" y2="1">
        <stop offset="0" stop-color="#e9d27c"/><stop offset="1" stop-color="#8c6d22"/>
      </linearGradient>
    </defs>
    <rect x="0" y="0" width="726" height="107" fill="#0b0b0b"/>
    <polygon points="415,40 455,40 250,400 210,400" fill="url(#goldBandBack)" opacity=".7"/>
    <polygon points="705,150 726,150 726,200 690,265 668,265" fill="url(#goldBandBack)" opacity=".7"/>
    <polyline points="0,107 400,107 440,40 726,40" fill="none" stroke="#c9a94a" stroke-width="2.5"/>
    <polygon points="0,464 726,464 726,512 0,512" fill="#0b0b0b"/>
    <line x1="0" y1="458" x2="726" y2="458" stroke="#c9a94a" stroke-width="2.5"/>
    <polygon points="490,464 726,464 726,512 468,512" fill="url(#goldBandBack)"/>
  </svg>

  <div class="brand"><span class="brand__square"></span><span class="brand__name">PushAndDuel</span></div>
  <p class="tagline">Premium quality<br>products for all lifting<br>and fighting sports</p>
  <div class="social"><span class="social__dot"></span><span class="social__dot"></span><span class="social__dot"></span></div>

  <h2 class="collections-title">OUR COLLECTIONS</h2>
  <div class="collections-text">
    <p>PushAndDuel is dedicated to get you Premium Quality Products for all Lifting and Fighting Sports.</p>
    <p>We focus on Customer Support and getting you products which assists you on reaching new personal records</p>
  </div>

  <div class="range" style="left:43px"><div class="medallion"><div class="medallion__art" role="img" aria-label="Torvik brand artwork"></div></div><p class="range__name">TORVIK</p><p class="range__sport">Powerlifting</p></div>
  <div class="range" style="left:175px"><div class="medallion"><div class="medallion__art" role="img" aria-label="ZL Boxing brand artwork"></div></div><p class="range__name">ZL BOXING</p><p class="range__sport">Boxing</p></div>
  <div class="range" style="left:307px"><div class="medallion"><div class="medallion__art" role="img" aria-label="Murelt brand artwork"></div></div><p class="range__name">MURELT</p><p class="range__sport">Martial Arts</p></div>
  <div class="range" style="left:439px"><div class="medallion"><div class="medallion__art" role="img" aria-label="PitVolt brand artwork"></div></div><p class="range__name">PITVOLT</p><p class="range__sport">MMA</p></div>
  <div class="range" style="left:571px"><div class="medallion"><div class="medallion__art" role="img" aria-label="Bramfold brand artwork"></div></div><p class="range__name">BRAMFOLD</p><p class="range__sport">Bodybuilding</p></div>

  <footer class="footer">
    <div class="footer__contact">
      <svg width="9" height="12" viewBox="0 0 9 12"><path d="M4.5 0A4.5 4.5 0 0 0 0 4.5C0 8 4.5 12 4.5 12S9 8 9 4.5A4.5 4.5 0 0 0 4.5 0zm0 6.3a1.8 1.8 0 1 1 0-3.6 1.8 1.8 0 0 1 0 3.6z" fill="#c9a94a"/></svg>
      <span>NORVAK UG Lindenweg 4, 01234 Musterstadt</span>
      <span class="footer__gap"></span>
      <svg width="13" height="9" viewBox="0 0 13 9"><rect width="13" height="9" fill="#c9a94a"/><path d="M0 0l6.5 5L13 0" stroke="#0b0b0b" fill="none"/></svg>
      <span>info@norvak.example</span>
    </div>
    <div class="footer__web">
      <svg width="16" height="16" viewBox="0 0 16 16"><circle cx="8" cy="8" r="7" fill="none" stroke="#0b0b0b" stroke-width="1.6"/><ellipse cx="8" cy="8" rx="3" ry="7" fill="none" stroke="#0b0b0b" stroke-width="1.2"/><line x1="1" y1="8" x2="15" y2="8" stroke="#0b0b0b" stroke-width="1.2"/></svg>
      <span>www.pushandduel.example</span>
    </div>
  </footer>
</section>

</body>
</html>
```